signboard Pranmeko

Hi, We are a language school and we register students abroad in Germany. We-have a lot of department and we need a signboard For Each department so students can Distinguish Each department. The design is the Sámi for all the departments. Only texts changes. List of departments: - Visa - Pre-university enrollment - Translations - Language school - Sales We need a Design that respect our logo colors, with our logo Thank u Waiting for proposals

Industry/Entity Type

School

```html
<!DOCTYPE html>
<html lang="fr">
<head>
<meta charset="utf-8">
<title>Pranmeko – signalétique des départements</title>
<link rel="stylesheet" href="https://fonts.googleapis.com/css2?family=Anton&display=swap">
<style>
  :root {
    --sign-yellow: #dfe22c;
    --ink: #231f20;
    --paper: #ffffff;
  }
  * { margin: 0; padding: 0; box-sizing: border-box; }
  html, body {
    width: 1200px;
    height: 1126px;
    overflow: hidden;
    background: var(--paper);
  }
  .board {
    position: relative;
    width: 1200px;
    height: 1126px;
  }
  .sign {
    position: absolute;
    width: 573px;
    height: 278px;
  }
  .sign--translations { left: 10px;  top: 78px; }
  .sign--language     { left: 616px; top: 78px; }
  .sign--visa         { left: 10px;  top: 436px; }
  .sign--sales        { left: 616px; top: 436px; }
  .sign--enrollment   { left: 314px; top: 782px; }

  .sign__art {
    display: block;
    width: 100%;
    height: 100%;
  }
  .sign__line {
    font-family: "Anton", "Oswald", sans-serif;
    text-transform: uppercase;
    text-anchor: middle;
    paint-order: stroke fill;
    stroke-linejoin: round;
  }
  .sign__line--light {
    fill: var(--paper);
    stroke: var(--ink);
    stroke-width: 8px;
  }
  .sign__line--dark {
    fill: var(--ink);
    stroke: var(--paper);
    stroke-width: 7px;
  }
  .sign__line--bold-outline { stroke-width: 11px; }
</style>
</head>
<body>
<svg width="0" height="0" style="position:absolute" aria-hidden="true">
  <defs>
    <symbol id="plate" viewBox="0 0 716 348">
      <path fill="var(--ink)"
        d="M65,0 H651 A50,50 0 0 0 700,48 V60 H716 V288 H700 V300 A50,50 0 0 0 651,348 H65 A50,50 0 0 0 16,300 V288 H0 V60 H16 V48 A50,50 0 0 0 65,0 Z"/>
      <path fill="var(--sign-yellow)" stroke="var(--paper)" stroke-width="9"
        d="M73,12 H643 A42,42 0 0 0 688,55 V68 H704 V280 H688 V293 A42,42 0 0 0 643,336 H73 A42,42 0 0 0 28,293 V280 H12 V68 H28 V55 A42,42 0 0 0 73,12 Z"/>
      <path fill="none" stroke="var(--ink)" stroke-width="2.5"
        d="M73,12 H643 A42,42 0 0 0 688,55 V68 H704 V280 H688 V293 A42,42 0 0 0 643,336 H73 A42,42 0 0 0 28,293 V280 H12 V68 H28 V55 A42,42 0 0 0 73,12 Z"/>
    </symbol>
  </defs>
</svg>

<main class="board">
  <section class="sign sign--translations">
    <svg class="sign__art" viewBox="0 0 716 348">
      <use href="#plate"/>
      <text class="sign__line sign__line--light" x="357" y="221" font-size="120"
        textLength="640" lengthAdjust="spacingAndGlyphs">Traductions</text>
    </svg>
  </section>

  <section class="sign sign--language">
    <svg class="sign__art" viewBox="0 0 716 348">
      <use href="#plate"/>
      <text class="sign__line sign__line--dark" x="354" y="154" font-size="118"
        textLength="418" lengthAdjust="spacingAndGlyphs">Ecole de</text>
      <text class="sign__line sign__line--light" x="354" y="299" font-size="150"
        textLength="424" lengthAdjust="spacingAndGlyphs">Langue</text>
    </svg>
  </section>

  <section class="sign sign--visa">
    <svg class="sign__art" viewBox="0 0 716 348">
      <use href="#plate"/>
      <text class="sign__line sign__line--light sign__line--bold-outline" x="356" y="282" font-size="262"
        textLength="446" lengthAdjust="spacingAndGlyphs">Visa</text>
    </svg>
  </section>

  <section class="sign sign--sales">
    <svg class="sign__art" viewBox="0 0 716 348">
      <use href="#plate"/>
      <text class="sign__line sign__line--light sign__line--bold-outline" x="352" y="262" font-size="207"
        textLength="570" lengthAdjust="spacingAndGlyphs">Ventes</text>
    </svg>
  </section>

  <section class="sign sign--enrollment">
    <svg class="sign__art" viewBox="0 0 716 348">
      <use href="#plate"/>
      <text class="sign__line sign__line--dark" x="355" y="154" font-size="88"
        textLength="624" lengthAdjust="spacingAndGlyphs">Pré-inscriptions</text>
      <text class="sign__line sign__line--light" x="357" y="270" font-size="111"
        textLength="634" lengthAdjust="spacingAndGlyphs">Universitaires</text>
    </svg>
  </section>
</main>
</body>
</html>
```